Keldro Cybersecurity Secives professional web site

Keldro is a unit of the Vostemic company, based on the audit services it offers and which mainly works by the contacts it has from its previous experience. The objective with the development of this website will be to increase its presence on the internet and even link the traffic of its social networks with the blog of the new page and in this way, provide information for old and potential customers.
For this reason, we will set the objective of the page, have all the information of the company, its services and its scope in general, in a formal and simple for users, facilitating the task of finding the information they want within of the page, as well as, including the option of feedback.
Updates

Need extra days to review

Target Market(s)

any company that needs security assessments

Number of Pages Required

4 page

Font styles to use
Sans Serif

Colors

Designer to choose colors to be used in the design.

Requirements
Must have
• READ THE PDF PLEASE. Video in homepage, cool graphics, color like our logo
• I like the following sites: www.vostemic-example.com & www.gantrelo-example.com
Nice to have
• Futuristic
Should not have
• Please, dont use the gallery pictures I used in my document, I prefer hand made illustrations instead

```html
<!DOCTYPE html>
<html lang="en">
<head>
<meta charset="utf-8">
<title>Keldro — Contact</title>
<link rel="stylesheet" href="https://fonts.googleapis.com/css2?family=Roboto:wght@400;500;700&display=swap">
<style>
  :root {
    --page-bg: #b3b3b3;
    --white: #ffffff;
    --navy: #1b2b42;
    --navy-deep: #16253a;
    --navy-light: #24374f;
    --ink: #2a2f36;
    --card: rgba(52, 54, 60, 0.78);
    --card-line: #e8e8e8;
    --map-tone: #e9ebe8;
  }
  * { margin: 0; padding: 0; box-sizing: border-box; }
  html, body {
    width: 1200px; height: 1200px; overflow: hidden;
    background: var(--page-bg);
    font-family: "Roboto", Arial, sans-serif;
  }
  .site {
    position: absolute; left: 202px; top: 323px;
    width: 797px; height: 555px;
    background: var(--white);
    border: 1px solid #d0d0d0;
  }
  .site-header { position: absolute; left: 0; top: 0; width: 100%; height: 68px; }
  .brand {
    position: absolute; left: 46px; top: 24px;
    color: var(--navy); font-weight: 700; font-size: 20px;
    line-height: 20px; letter-spacing: 0.3px;
  }
  .main-nav a {
    position: absolute; top: 34px;
    color: var(--ink); font-weight: 700; font-size: 11px;
    text-decoration: none; letter-spacing: 0.2px;
  }
  .main-nav a.is-current::after {
    content: ""; position: absolute; left: 0; top: 17px;
    width: 52px; height: 2px; background: #3a3a3a;
  }
  .header-social { position: absolute; top: 18px; left: 703px; display: flex; gap: 15px; }
  .header-social span { width: 11px; height: 11px; display: block; }
  .dot { border-radius: 50%; background: var(--ink); }

  .hero {
    position: absolute; left: 0; top: 68px; width: 100%; height: 418px;
    background:
      radial-gradient(circle at 30% 40%, rgba(70, 95, 125, 0.35), transparent 45%),
      radial-gradient(circle at 75% 75%, rgba(60, 85, 115, 0.3), transparent 40%),
      linear-gradient(160deg, var(--navy-light), var(--navy) 55%, var(--navy-deep));
  }
  .card {
    position: absolute; top: 90px; width: 292px; height: 242px;
    background: var(--card);
  }
  .contact-card { left: 88px; color: var(--white); }
  .contact-title {
    position: absolute; left: 12px; top: 22px;
    font-size: 13px; font-weight: 400;
  }
  .contact-title::after {
    content: ""; position: absolute; left: 0; top: 25px;
    width: 251px; height: 1px; background: var(--card-line);
  }
  .contact-item { position: absolute; left: 16px; display: flex; align-items: center; gap: 14px; font-size: 10.5px; line-height: 13px; }
  .contact-item svg { width: 20px; height: 20px; flex: none; }
  .item-phone { top: 73px; }
  .item-web { top: 121px; }
  .item-web span { padding-left: 3px; }
  .item-address { top: 170px; }

  .map-card { left: 433px; }
  .map-area {
    position: absolute; left: 20px; top: 21px; width: 253px; height: 198px;
    background: linear-gradient(135deg, #eef0ed, var(--map-tone) 60%, #dfe6e0);
    border: 1px solid #ffffff;
  }

  .site-footer { position: absolute; left: 0; top: 486px; width: 100%; height: 69px; }
  .footer-link {
    position: absolute; top: 28px; display: flex; align-items: center; gap: 4px;
    color: var(--ink); font-size: 10.5px; letter-spacing: 0.8px; text-decoration: none;
  }
  .footer-link .dot { width: 9px; height: 9px; }
  .footer-link svg { width: 10px; height: 10px; }
</style>
</head>
<body>
<div class="site">
  <header class="site-header">
    <div class="brand">KELDRO</div>
    <nav class="main-nav">
      <a href="#" style="left:241px">HOME</a>
      <a href="#" style="left:323px">COMPANY</a>
      <a href="#" style="left:427px">SERVICES</a>
      <a href="#" style="left:531px">BLOG</a>
      <a href="#" class="is-current" style="left:613px">CONTACT</a>
    </nav>
    <div class="header-social">
      <span class="dot"></span>
      <span class="dot"></span>
      <span>
        <svg viewBox="0 0 12 12" width="11" height="11" fill="none" stroke="#2a2f36" stroke-width="1.2">
          <rect x="1" y="1" width="10" height="10" rx="1.5"/><path d="M3 4h6M3 6h6M3 8h4"/>
        </svg>
      </span>
    </div>
  </header>

  <section class="hero">
    <div class="card contact-card">
      <h1 class="contact-title">Contact us, we will be happy to assist you.</h1>
      <div class="contact-item item-phone">
        <svg viewBox="0 0 24 24" fill="none" stroke="#fff" stroke-width="1.1">
          <path d="M6 3l3 4-2 2c1 3 4 6 7 7l2-2 4 3-2 3c-8 0-15-7-15-15z"/>
          <path d="M14 4a6 6 0 0 1 6 6M14 7a3 3 0 0 1 3 3"/>
        </svg>
        <div>+34 900 555 142<br>(working hours 9:00-19:00 in summer (8:00-13:00)</div>
      </div>
      <div class="contact-item item-web">
        <svg viewBox="0 0 24 24" fill="none" stroke="#fff" stroke-width="1.1">
          <rect x="2" y="5" width="20" height="14"/><path d="M2 5l10 8 10-8M2 19l7-7M22 19l-7-7"/>
        </svg>
        <span>www.keldrosecurity-example.com</span>
      </div>
      <div class="contact-item item-address">
        <svg viewBox="0 0 24 24" fill="none" stroke="#fff" stroke-width="1.1">
          <path d="M12 17s-5-5-5-9a5 5 0 0 1 10 0c0 4-5 9-5 9z"/><circle cx="12" cy="8" r="2"/>
          <path d="M7 16l-4 5h18l-4-5"/>
        </svg>
        <div>Av. Sorvela, 14<br>24090 Valmira<br>Valmira España</div>
      </div>
    </div>
    <div class="card map-card">
      <div class="map-area" role="img" aria-label="Street map showing the office location"></div>
    </div>
  </section>

  <footer class="site-footer">
    <a href="#" class="footer-link" style="left:281px"><span class="dot"></span>Chirp</a>
    <a href="#" class="footer-link" style="left:366px"><span class="dot"></span>Snapgram</a>
    <a href="#" class="footer-link" style="left:466px">
      <svg viewBox="0 0 12 12" fill="none" stroke="#2a2f36" stroke-width="1.2">
        <rect x="1" y="1" width="10" height="10" rx="1.5"/><path d="M3 4h6M3 6h6M3 8h4"/>
      </svg>Blog</a>
  </footer>
</div>
</body>
</html>
```